Torvelin Business Card

We need a business card design. We have a logo from a previous PixelHarbor project and I am attaching the logo files in jpeg and photoshop.

Business

```html
<!DOCTYPE html>
<html lang="en">
<head>
<meta charset="utf-8">
<title>Torvelin Business Card</title>
<link rel="stylesheet" href="https://fonts.googleapis.com/css2?family=Open+Sans:wght@400;600;700&display=swap">
<style>
  :root {
    --backdrop: #e7e4df;
    --card-white: #ffffff;
    --panel-grey: #404040;
    --brand-green: #3fb24a;
    --ink-dark: #3b3b3b;
    --text-light: #f4f4f4;
  }
  * { box-sizing: border-box; margin: 0; padding: 0; }
  html, body {
    width: 1200px;
    height: 865px;
    overflow: hidden;
    background: var(--backdrop);
    font-family: "Open Sans", Arial, sans-serif;
  }
  .canvas {
    width: 1200px;
    height: 865px;
    display: flex;
    align-items: center;
    justify-content: center;
  }
  .business-card {
    position: relative;
    width: 900px;
    height: 514px;
    background: var(--card-white);
    box-shadow: 0 10px 30px rgba(0, 0, 0, 0.18);
    overflow: hidden;
  }
  .card-header {
    height: 196px;
    display: flex;
    align-items: center;
    padding-left: 82px;
    gap: 18px;
  }
  .brand-square {
    width: 38px;
    height: 38px;
    background: var(--brand-green);
  }
  .brand-name {
    font-size: 60px;
    font-weight: 700;
    letter-spacing: -1px;
    color: var(--ink-dark);
    line-height: 1;
  }
  .accent-line {
    height: 3px;
    background: var(--brand-green);
  }
  .card-panel {
    position: absolute;
    top: 199px;
    left: 0;
    right: 0;
    bottom: 0;
    background: var(--panel-grey);
  }
  .person {
    position: absolute;
    left: 82px;
    top: 40px;
  }
  .person-name {
    font-size: 44px;
    font-weight: 600;
    color: var(--brand-green);
    line-height: 1.1;
  }
  .person-role {
    font-size: 24px;
    color: var(--text-light);
    margin-top: 2px;
  }
  .contact-list {
    position: absolute;
    left: 560px;
    top: 120px;
    list-style: none;
    color: var(--text-light);
    font-size: 22px;
    line-height: 30px;
  }
  .contact-item {
    display: flex;
    align-items: flex-start;
    gap: 18px;
  }
  .contact-icon {
    width: 20px;
    height: 20px;
    margin-top: 5px;
    flex-shrink: 0;
  }
  .contact-icon * {
    fill: none;
    stroke: var(--brand-green);
    stroke-width: 2;
    stroke-linecap: round;
    stroke-linejoin: round;
  }
  .contact-icon .solid { fill: var(--brand-green); stroke: none; }
  .postcode { margin-left: 22px; }
</style>
</head>
<body>
<main class="canvas">
  <article class="business-card">
    <header class="card-header">
      <span class="brand-square" aria-hidden="true"></span>
      <span class="brand-name">Torvelin</span>
    </header>
    <div class="accent-line"></div>
    <section class="card-panel">
      <div class="person">
        <p class="person-name">Your Name</p>
        <p class="person-role">Your Role</p>
      </div>
      <ul class="contact-list">
        <li class="contact-item">
          <svg class="contact-icon" viewBox="0 0 20 20" aria-hidden="true">
            <path class="solid" d="M5 2 L8 2 L9 6 L7 8 Q9 12 12 13 L14 11 L18 12 L18 15 Q17 18 14 18 Q4 16 2 6 Q2 3 5 2 Z"/>
          </svg>
          <span>999 999 999</span>
        </li>
        <li class="contact-item">
          <svg class="contact-icon" viewBox="0 0 20 20" aria-hidden="true">
            <rect x="2" y="4" width="16" height="12"/>
            <path d="M2 4 L10 11 L18 4"/>
          </svg>
          <span>sample@postlane.com</span>
        </li>
        <li class="contact-item">
          <svg class="contact-icon" viewBox="0 0 20 20" aria-hidden="true">
            <path d="M17 17 L4 4"/>
            <path d="M4 12 L4 4 L12 4"/>
          </svg>
          <span>www.sample.com</span>
        </li>
        <li class="contact-item">
          <svg class="contact-icon" viewBox="0 0 20 20" aria-hidden="true">
            <path d="M2 10 L10 3 L18 10"/>
            <path d="M4 9 L4 17 L16 17 L16 9"/>
            <rect x="8" y="11" width="4" height="6"/>
          </svg>
          <span>999 Sample St,<br>Area<br>City<span class="postcode">Postcode</span></span>
        </li>
      </ul>
    </section>
  </article>
</main>
</body>
</html>
```